Geschäftspapiere für unternehmerische Holding für Beteiligungen, Projektgesellschaften und kaufmännische Steuerung
Zielgruppe
Die Hollwen GmbH ist eine unternehmerische Holding für Beteiligungen, Projektgesellschaften und kaufmännische Steuerung. Sie übernimmt Management-, Controlling- und Strukturierungsaufgaben für verbundene Unternehmen.
Zielgruppe sind Banken, Investoren, Geschäftspartner, Steuerberater, Rechtsanwälte, Behörden sowie Geschäftsführungen und Gesellschafter von Beteiligungs- und Projektgesellschaften.
Aufgabenstellung
Gesucht wird ein digitales Briefpapier für die Hollwen GmbH, das sowohl als PDF/Dokumentvorlage als auch beim Ausdruck professionell funktioniert.
Wichtig ist ein sehr klarer, hochwertiger und seriöser Auftritt. Das Design soll reduziert, strukturiert und geschäftlich wirken – keine verspielten Elemente, keine überladenen Grafiken, keine auffälligen Muster.
Das Briefpapier muss drucktauglich sein. Bitte ausreichende Druckränder und Sicherheitsabstände berücksichtigen, damit Kopf- und Fußbereich auch auf normalen Büro- und Laserdruckern sauber ausgegeben werden können. Das Layout soll sowohl digital als auch gedruckt stimmig aussehen.
Format: DIN A4 Hochformat.
Gewünschte Inhalte:
* Logo der Hollwen GmbH
* Firmenname: Hollwen GmbH
* Geschäftsanschrift: Lindauer Weg 52, 80339 München
* Telefon: 089 58210946
* E-Mail: info@hollwenbeta.example
* Webseite: hollwenbeta.example
* Geschäftsführung: Dipl.-Wirtschaftsing. (FH) Till Osterwald
* Registergericht / Amtsgericht München HRB 527081
* Bankverbindung IBAN DE918204 5571 0009 1826 40
Besonderer Wert liegt auf:
* hochwertiger Holding-/Investment-Anmutung
* sehr guter Lesbarkeit
* klarer Kopf- und Fußzeile
* sauberer Typografie
* professioneller Nutzbarkeit für Angebote, Verträge, Behörden- und Bankkorrespondenz
Bitte das Design so anlegen, dass es später als editierbare Word-/PDF-Vorlage genutzt werden kann und sowohl das Logo, als auch die Farben entsprechend verwenden.

```html
<!DOCTYPE html>
<html lang="de">
<head>
<meta charset="utf-8">
<title>Hollwen GmbH – Briefpapier</title>
<link rel="stylesheet" href="https://fonts.googleapis.com/css2?family=Arimo:wght@400&family=Open+Sans:wght@400;600&display=swap">
<style>
  :root {
    --navy: #0f1a33;
    --ink: #1b1b1b;
    --muted: #3a3a3a;
    --paper: #ffffff;
    --backdrop: #e6e7ea;
    --signature: #1f2f9c;
  }
  html, body {
    margin: 0; padding: 0;
    width: 1200px; height: 1010px;
    overflow: hidden;
    background: var(--backdrop);
  }
  .sheet {
    position: absolute;
    left: 260px; top: 24px;
    width: 680px; height: 962px;
    background: var(--paper);
    box-shadow: 0 2px 10px rgba(0,0,0,0.12);
    font-family: "Arimo", Arial, sans-serif;
    color: var(--ink);
  }
  .top-rule {
    position: absolute; left: 40px; right: 40px; top: 30px;
    height: 6px; background: var(--navy);
  }
  .brand {
    position: absolute; right: 44px; top: 62px;
    font-family: "Open Sans", Arial, sans-serif;
    font-weight: 400; font-size: 46px; letter-spacing: 6px;
    text-transform: uppercase; color: var(--navy);
    display: flex; align-items: center; gap: 12px;
  }
  .brand-mark { width: 12px; height: 12px; background: var(--navy); }
  .contact {
    position: absolute; right: 44px; top: 138px;
    width: 170px; padding-left: 12px;
    border-left: 1px solid var(--navy);
    font-family: "Open Sans", Arial, sans-serif;
    font-size: 9.5px; line-height: 1.45; color: var(--muted);
  }
  .contact p { margin: 0; }
  .contact .gap { height: 6px; }
  .contact .row { display: flex; align-items: center; gap: 6px; }
  .contact svg { width: 9px; height: 9px; fill: var(--navy); flex: none; }
  .return-line {
    position: absolute; left: 70px; top: 196px;
    font-family: "Open Sans", Arial, sans-serif;
    font-size: 7.5px; color: var(--muted);
    border-bottom: 1px solid var(--muted); padding-bottom: 1px;
  }
  .recipient {
    position: absolute; left: 70px; top: 218px;
    font-size: 12px; line-height: 1.35;
  }
  .recipient p { margin: 0; }
  .recipient .city { margin-top: 12px; }
  .letter {
    position: absolute; left: 70px; right: 70px; top: 330px;
    font-size: 12px; line-height: 1.38;
  }
  .letter p { margin: 0 0 16px; text-align: justify; }
  .letter .closing { margin-top: 20px; margin-bottom: 0; }
  .signature {
    width: 200px; height: 46px; margin: 6px 0 4px;
    background: linear-gradient(90deg, rgba(31,47,156,0.18), rgba(31,47,156,0.06));
    border-radius: 4px;
  }
  .signer { margin: 0; }
  .footer {
    position: absolute; left: 0; right: 0; bottom: 30px;
    height: 78px; background: var(--navy);
    display: flex; align-items: center;
    font-family: "Open Sans", Arial, sans-serif;
    font-size: 9px; line-height: 1.45; color: #ffffff;
  }
  .footer-col { flex: 1; padding: 0 28px; }
  .footer-col p { margin: 0; }
  .footer-col + .footer-col { border-left: 1px solid rgba(255,255,255,0.7); }
  .footer-col.mid { text-align: center; }
  .footer-col.right { text-align: right; }
</style>
</head>
<body>
<div class="sheet">
  <div class="top-rule"></div>

  <div class="brand"><span class="brand-mark"></span>Hollwen</div>

  <div class="contact">
    <p>Hollwen GmbH</p>
    <p>Lindauer Weg 52</p>
    <p>80339 München</p>
    <div class="gap"></div>
    <p class="row"><svg viewBox="0 0 24 24"><path d="M6.6 10.8a15 15 0 0 0 6.6 6.6l2.2-2.2c.3-.3.7-.4 1-.2 1.1.4 2.3.6 3.6.6.6 0 1 .4 1 1V20c0 .6-.4 1-1 1A17 17 0 0 1 3 4c0-.6.4-1 1-1h3.5c.6 0 1 .4 1 1 0 1.3.2 2.5.6 3.6.1.3 0 .7-.2 1z"/></svg>+49 (0)89 58210946</p>
    <p class="row"><svg viewBox="0 0 24 24"><path d="M2 5h20v14H2zm2 2v.5l8 5 8-5V7l-8 5z"/></svg>info@hollwenbeta.example</p>
    <p class="row"><svg viewBox="0 0 24 24"><circle cx="12" cy="12" r="10"/></svg>hollwenbeta.example</p>
  </div>

  <div class="return-line">Hollwen GmbH | Lindauer Weg 52 | 80339 München</div>

  <div class="recipient">
    <p>Musterfirma</p>
    <p>z. Hd. Herrn Mustermann</p>
    <p>Musterweg 13</p>
    <p class="city">24102 Musterstadt</p>
  </div>

  <div class="letter">
    <p>Sehr geehrte Damen und Herren,</p>
    <p>In sollicitudin, metus et posuere blandit, erat dui bibendum eros, id vestibulum sem justo vel mauris. Ut tempor dolor ut justo vulputate, eu blandit libero faucibus. In laoreet, massa non ultricies tempor, est enim auctor mi, sit amet venenatis massa augue in justo. Praesent eu tincidunt diam. Maecenas id mi efficitur tellus interdum consectetur vel sed ante. Sed suscipit quis eros a fermentum. Curabitur ornare sit amet leo eu semper. Vestibulum pretium mi eu nisi.</p>
    <p>Sed nunc est, iaculis vel enim ut, fringilla commodo lorem. Pellentesque facilisis tempus lorem eget porttitor. Morbi accumsan, nulla accumsan mollis maximus, lectus diam venenatis odio, quis bibendum elit ex a arcu. Fusce turpis erat, euismod sit amet dolor eu, hendrerit rhoncus libero. Phasellus convallis, mi vel pharetra sollicitudin, nisi purus maximus est, nec lobortis dolor enim et augue. Vestibulum auctor mi sit amet leo auctor egestas. Pellentesque eget endrerit rhoncus dan.</p>
    <p class="closing">Mit freundlichen Grüßen</p>
    <div class="signature" role="img" aria-label="Handschriftliche Unterschrift von Till Osterwald"></div>
    <p class="signer">Till Osterwald</p>
  </div>

  <div class="footer">
    <div class="footer-col">
      <p>Amtsgericht München</p>
      <p>HRB 527081</p>
      <p>Sitz der Gesellschaft: München</p>
      <p>USt-ID.: DE417590362</p>
    </div>
    <div class="footer-col mid">
      <p>Geschäftsführer:</p>
      <p>Till Osterwald</p>
    </div>
    <div class="footer-col right">
      <p>Talbrunn Privatbank Salzburg</p>
      <p>AT61 4820 7000 3100 2288</p>
      <p>Genossenschaftsbank Isarauen</p>
      <p>DE918204 5571 0009 1826 40</p>
    </div>
  </div>
</div>
</body>
</html>
```